Business Card Design

We need a business card for a well established Semi Trailer Hire company. I am looking for a new start as we are moving so would like to update our Business Cards and Letter heads.
We hire Semi Trailers to Transport companies.
The colour of our Trailers are Cherry Red so this must be the prominent colour.
I do not want any pictures of trailers on the design.
I do not want the design to be flowery in anyway as we are in the transport industry.
Simple yet effective

Trovan Hire Pty Ltd
Ros Dunmore
Director
Ph: 03 9412 5083
Mobile: 0421 736 209
ros.dunmore@trovanhire.com.au
www.trovanhire.com.au
214-220 Pellow Road, Yarraville

```html
<!DOCTYPE html>
<html lang="en">
<head>
<meta charset="utf-8">
<title>Trovan Hire Pty Ltd — Business Card</title>
<link href="https://fonts.googleapis.com/css2?family=Oswald:wght@400;600&family=Roboto+Condensed:wght@400;700&display=swap" rel="stylesheet">
<style>
  :root {
    --cherry: #b3121c;
    --cherry-deep: #7d0a12;
    --cherry-bright: #d8222c;
    --paper: #ffffff;
    --ink: #1c1c1c;
    --silver: #e6e6e6;
    --backdrop: #e9e6e2;
  }
  * { margin: 0; padding: 0; box-sizing: border-box; }
  html, body { width: 1200px; height: 900px; overflow: hidden; }
  body {
    background: var(--backdrop);
    font-family: "Roboto Condensed", sans-serif;
    position: relative;
  }
  .card {
    position: absolute;
    top: 300px;
    width: 525px;
    height: 300px;
    border-radius: 4px;
    overflow: hidden;
    box-shadow: 0 10px 24px rgba(0,0,0,0.18);
  }
  .card--front {
    left: 50px;
    background:
      radial-gradient(ellipse at 45% 40%, rgba(255,255,255,0.22) 0%, rgba(255,255,255,0) 45%),
      radial-gradient(circle at 50% 50%, var(--cherry-bright) 0%, var(--cherry) 55%, var(--cherry-deep) 100%);
    display: flex;
    align-items: center;
    justify-content: center;
  }
  .front-name {
    text-align: center;
    color: var(--silver);
    font-family: "Oswald", sans-serif;
    font-weight: 400;
  }
  .front-name__main {
    font-size: 44px;
    letter-spacing: 14px;
    line-height: 1.1;
    padding-left: 14px;
  }
  .front-name__sub {
    font-size: 18px;
    letter-spacing: 4px;
    margin-top: 4px;
  }
  .card--back {
    left: 625px;
    background: var(--paper);
  }
  .back-band {
    position: absolute;
    inset: 0;
    width: 100%;
    height: 100%;
  }
  .back-content {
    position: absolute;
    left: 34px;
    top: 28px;
    right: 30px;
  }
  .company {
    font-family: "Oswald", sans-serif;
    font-weight: 600;
    color: var(--cherry);
    font-size: 26px;
    line-height: 1.05;
    text-transform: uppercase;
    padding-bottom: 6px;
  }
  .address {
    font-size: 13px;
    font-weight: 700;
    color: var(--ink);
    padding-bottom: 12px;
    border-bottom: 1.5px solid var(--cherry);
    width: 260px;
  }
  .person { margin-top: 14px; }
  .person__name {
    font-family: "Oswald", sans-serif;
    font-weight: 600;
    color: var(--cherry);
    font-size: 17px;
    text-transform: uppercase;
    letter-spacing: 0.5px;
  }
  .person__role { font-size: 12px; font-weight: 700; color: var(--ink); }
  .contacts { list-style: none; margin-top: 12px; }
  .contacts li {
    display: flex;
    align-items: center;
    gap: 8px;
    font-size: 13.5px;
    color: var(--ink);
    line-height: 20px;
  }
  .contacts svg { width: 13px; height: 13px; flex: none; }
</style>
</head>
<body>

<section class="card card--front" aria-label="Card front">
  <div class="front-name">
    <div class="front-name__main">TROVAN</div>
    <div class="front-name__sub">HIRE PTY LTD</div>
  </div>
</section>

<section class="card card--back" aria-label="Card back">
  <svg class="back-band" viewBox="0 0 525 300" preserveAspectRatio="none" aria-hidden="true">
    <defs>
      <linearGradient id="band-shade" x1="0" y1="0" x2="1" y2="1">
        <stop offset="0" stop-color="#c4161f"/>
        <stop offset="1" stop-color="#7d0a12"/>
      </linearGradient>
    </defs>
    <path d="M0 300 L0 272 Q300 268 525 160 L525 300 Z" fill="url(#band-shade)"/>
  </svg>

  <div class="back-content">
    <div class="company">Trovan Hire<br>Pty Ltd</div>
    <div class="address">214-220 Pellow Road, Yarraville</div>

    <div class="person">
      <div class="person__name">Ros Dunmore</div>
      <div class="person__role">Director</div>
    </div>

    <ul class="contacts">
      <li>
        <svg viewBox="0 0 14 14" aria-hidden="true"><circle cx="7" cy="7" r="7" fill="var(--cherry)"/><path d="M4.3 3.6c.4-.3.8-.2 1 .2l.6 1.2c.1.3 0 .6-.2.8l-.4.3c.4.9 1 1.5 1.9 1.9l.3-.4c.2-.2.5-.3.8-.2l1.2.6c.4.2.5.6.2 1l-.5.6c-.4.4-1 .5-1.6.2C6 9.2 4.8 8 4 6.4c-.3-.6-.2-1.2.2-1.6z" fill="#fff"/></svg>
        03 9412 5083
      </li>
      <li>
        <svg viewBox="0 0 14 14" aria-hidden="true"><circle cx="7" cy="7" r="7" fill="var(--cherry)"/><rect x="4.8" y="3" width="4.4" height="8" rx="0.8" fill="#fff"/><rect x="5.5" y="4" width="3" height="5" fill="var(--cherry)"/></svg>
        0421 736 209
      </li>
      <li>
        <svg viewBox="0 0 14 14" aria-hidden="true"><circle cx="7" cy="7" r="7" fill="var(--cherry)"/><rect x="3.5" y="4.5" width="7" height="5" fill="#fff"/><path d="M3.5 4.5 L7 7.3 L10.5 4.5" fill="none" stroke="var(--cherry)" stroke-width="0.8"/></svg>
        ros.dunmore@trovanhire.com.au
      </li>
      <li>
        <svg viewBox="0 0 14 14" aria-hidden="true"><circle cx="7" cy="7" r="7" fill="var(--cherry)"/><circle cx="7" cy="7" r="3.6" fill="none" stroke="#fff" stroke-width="0.9"/><path d="M3.4 7h7.2M7 3.4c-1.5 2-1.5 5.2 0 7.2M7 3.4c1.5 2 1.5 5.2 0 7.2" fill="none" stroke="#fff" stroke-width="0.7"/></svg>
        www.trovanhire.com.au
      </li>
    </ul>
  </div>
</section>

</body>
</html>
```